SipLoop Business Cards

Hi designers!

Here's some background on our start-up and this project:

SipLoop is a website that will allow users to order alcohol from nearby liquor stores and have it delivered to their homes in minutes. We are really excited to work on creating the best online, alcohol purchasing experience for the users.

So why SipLoop? We like to think of ourselves as that great friend who will get alcohol for you because he happens to have a car. We help you drink in with your friends, family, or guests. Our site will target students and young professionals (of drinking age) who are comfortable buying things online or through apps. We don't see this service as a luxury, VIP, or niche service in the least; instead, we think of us as a relaxed, service-driven start-up that believes in simple design and transparent .

Now, we want a business card that incorporates our newly acquired logo design and some complimenting colors and fonts. Feel free to do it single or double sided, although I'm a sucker for double...

If you happen to have any questions, want to throw some ideas around, or just want some feedback- email me at marco@siploop.example.

Marco Tessin
Founder

Industry/Entity Type

Business

Requirements
Must have
• Name, Position, Email, Cell-phone

No address, no fax, no land-line.

```html
<!DOCTYPE html>
<html lang="en">
<head>
<meta charset="utf-8">
<title>SipLoop Business Cards</title>
<link rel="stylesheet" href="https://fonts.googleapis.com/css2?family=Arimo:wght@400;700&display=swap">
<style>
  :root {
    --backdrop: #2a2a2a;
    --card: #f4f3f1;
    --ink: #111111;
    --accent: #f7c21e;
    --wordmark-faint: #a9a9a9;
  }
  * { margin: 0; padding: 0; box-sizing: border-box; }
  html, body {
    width: 1200px; height: 1000px; overflow: hidden;
    background: var(--backdrop);
    font-family: "Arimo", Arial, sans-serif;
    color: var(--ink);
  }
  .card {
    position: absolute;
    left: 327px;
    width: 553px;
    height: 297px;
    background: var(--card);
    border-radius: 14px;
  }
  .card--front { top: 166px; }
  .card--back { top: 549px; }

  .front-wordmark {
    position: absolute;
    left: 0; right: 0; top: 268px;
    text-align: center;
    font-weight: 700;
    font-size: 92px;
    letter-spacing: -2px;
    color: var(--wordmark-faint);
    opacity: 0.8;
    top: 100px;
    line-height: 1;
  }

  .contact {
    position: absolute;
    top: 226px;
    font-size: 15px;
    line-height: 1.45;
  }
  .contact__label { font-weight: 700; }
  .contact--person { left: 32px; }
  .contact--email { left: 228px; }
  .contact--tel { left: 414px; }
  .person__name { font-weight: 700; font-size: 18px; line-height: 1.1; }
  .person__surname { color: var(--accent); }
  .person__role { font-size: 11px; letter-spacing: 0.3px; }
  .contact__value { display: block; margin-top: 4px; }

  .back-wordmark {
    position: absolute;
    left: 93px; top: 128px;
    font-weight: 700;
    font-size: 46px;
    letter-spacing: -1px;
    line-height: 1;
    color: var(--ink);
  }
  .back-square {
    position: absolute;
    left: 302px; top: 77px;
    width: 145px; height: 145px;
    background: var(--accent);
  }
</style>
</head>
<body>
  <section class="card card--front">
    <div class="front-wordmark">SipLoop</div>
    <div class="contact contact--person">
      <div class="person__name">Marco <span class="person__surname">Tessin</span></div>
      <div class="person__role">DIRECTOR</div>
    </div>
    <div class="contact contact--email">
      <span class="contact__label">Email:</span>
      <span class="contact__value">marco@siploop.example</span>
    </div>
    <div class="contact contact--tel">
      <span class="contact__label">Tel:</span>
      <span class="contact__value">00-02-0318</span>
    </div>
  </section>

  <section class="card card--back">
    <div class="back-wordmark">SipLoop</div>
    <div class="back-square"></div>
  </section>
</body>
</html>
```